The Brightway Surgery Stationary (Medical)

Stationery for The Brightway surgery
using existing logos
Please also add a green apple if possible on another corner away from the logo on some of your designs

Please take a look at www.thebrightwaysurgery.com.au so you can get a feel for what The Brightway Surgery offers our clients.

Stationary Required: business cards, letter head, comp slips

I do not require envelopes or invoives.

Target Market(s)

The general popultation needing medical care
Professionals
Mums & Dads
Elderly

Industry/Entity Type

Business

Requirements
Must have
• Company Logo

Address
Email
Website
Phone
Should not have
• Traditional Medical Icons
No Times New Roman

```html
<!DOCTYPE html>
<html lang="en">
<head>
<meta charset="utf-8">
<title>The Brightway Surgery – Business Cards</title>
<link href="https://fonts.googleapis.com/css2?family=Didact+Gothic&family=Questrial&display=swap" rel="stylesheet">
<style>
  :root {
    --backdrop: #ebebeb;
    --card-white: #ffffff;
    --leaf-green: #5cb82e;
    --leaf-green-dark: #3f9a1c;
    --leaf-green-light: #9fd86a;
    --pale-apple: #e3f2cf;
    --sky-blue: #1b9ad6;
    --ink: #3a3a3a;
  }
  * { box-sizing: border-box; margin: 0; padding: 0; }
  html, body { width: 1200px; height: 900px; overflow: hidden; }
  body {
    background: radial-gradient(circle at 50% 40%, #f7f7f7 0%, var(--backdrop) 75%);
    position: relative;
    font-family: "Didact Gothic", sans-serif;
  }
  .card {
    position: absolute;
    width: 560px;
    height: 320px;
    overflow: hidden;
    box-shadow: 0 8px 22px rgba(0,0,0,0.18);
  }
  .card--front { left: 570px; top: 110px; background: var(--card-white); }
  .card--back {
    left: 80px; top: 470px;
    background: linear-gradient(135deg, var(--leaf-green-dark) 0%, var(--leaf-green) 45%, var(--leaf-green-light) 100%);
  }
  .edge-band {
    position: absolute; top: 0; right: 0;
    width: 36px; height: 100%;
    background: linear-gradient(180deg, var(--leaf-green) 0%, var(--leaf-green-dark) 100%);
  }
  .edge-square {
    position: absolute; right: 0; bottom: 0;
    width: 36px; height: 36px;
    background: var(--sky-blue);
  }
  .apple-photo {
    position: absolute; right: 48px; bottom: 22px;
    width: 110px; height: 104px;
    border-radius: 50%;
    background: radial-gradient(circle at 35% 30%, #b7eb6e 0%, #5fb623 45%, #2f7f0e 100%);
  }
  .apple-faint {
    position: absolute; left: 40px; top: 130px;
    width: 300px; height: 260px;
    border-radius: 50%;
    background: radial-gradient(circle at 50% 40%, #f2f9ea 0%, #dcedca 55%, rgba(220,237,202,0) 75%);
  }
  .apple-badge {
    position: absolute; left: 40px; top: 40px;
    width: 300px; height: 240px;
    border-radius: 50%;
    background: radial-gradient(circle at 45% 40%, #f4faec 0%, var(--pale-apple) 60%, #c9e6a8 100%);
    box-shadow: 0 6px 14px rgba(0,0,0,0.18);
  }
  .brand {
    position: absolute;
    display: flex; align-items: center; gap: 12px;
  }
  .card--front .brand { left: 40px; top: 40px; }
  .card--back .brand { left: 72px; top: 100px; }
  .brand__dot {
    width: 30px; height: 30px; border-radius: 50%;
    background: var(--sky-blue);
  }
  .brand__name {
    font-family: "Questrial", sans-serif;
    font-size: 30px; line-height: 1.05;
    color: var(--ink);
  }
  .tagline {
    position: absolute;
    font-size: 13px; line-height: 1.35;
    color: var(--ink);
    text-align: right;
    white-space: nowrap;
  }
  .card--front .tagline { left: 130px; top: 122px; width: 200px; }
  .card--back .tagline { left: 110px; top: 190px; width: 200px; }
</style>
</head>
<body>
  <section class="card card--front" aria-label="Business card front">
    <div class="apple-faint" role="img" aria-label="Large faint green apple photograph"></div>
    <div class="brand">
      <span class="brand__dot"></span>
      <span class="brand__name">The Brightway<br>Surgery</span>
    </div>
    <p class="tagline">Friendly Family Care<br>Close To Home, Always</p>
    <div class="edge-band"></div>
    <div class="edge-square"></div>
    <div class="apple-photo" role="img" aria-label="Green apple photograph with water droplets"></div>
  </section>

  <section class="card card--back" aria-label="Business card back">
    <div class="apple-badge" role="img" aria-label="Pale green apple shape behind the name"></div>
    <div class="brand">
      <span class="brand__dot"></span>
      <span class="brand__name">The Brightway<br>Surgery</span>
    </div>
    <p class="tagline">Friendly Family Care<br>Close To Home, Always</p>
    <div class="edge-band"></div>
    <div class="edge-square"></div>
    <div class="apple-photo" role="img" aria-label="Green apple photograph with water droplets"></div>
  </section>
</body>
</html>
```